Accounting Practice Business Card Design

I have a logo I am happy for you to use in the design of the Business Card.
You can edit and change colours as you please, I am not fixated on it.
I am looking for a modern and clean overall feel for the finished design.

The business is a small accounting practice who thrives on word of mouth referrals and this card will be given to all current and prospect clients.

Industry/Entity Type

Accountant

Contact Information for Business Card

Marcus Elwin
Level 5, 8 Corvale Ridge Road
ASHGROVE RISE VIC 3187
Phone: 9481 3057
Email: melwin@mrfaccountants.com.au
Web: www.mrfaccountants.com.au

Font styles to use
Serif
Sans Serif

Colors
0555a3
3277b5
85acd3
0393ce
33a6d7
85cae6
00a990
33b8a4
9bcb3c

Requirements
Must have
• "The end to your tax problems begin with us"
• "A referral from you is our greatest compliment"
Nice to have
• Modern clean professional

```html
<!DOCTYPE html>
<html lang="en">
<head>
<meta charset="utf-8">
<title>MRF Accountants – Business Card</title>
<link rel="stylesheet" href="https://fonts.googleapis.com/css2?family=Exo+2:wght@400;500;700;800&display=swap">
<style>
  :root {
    --page-bg: #e9e8e6;
    --card-bg: #1c1d1f;
    --card-edge: #2a2b2e;
    --brand-silver: #9a9c9f;
    --brand-blue: #1f62a8;
    --text-light: #e4e5e7;
    --divider: #6d6f73;
  }
  * { box-sizing: border-box; margin: 0; padding: 0; }
  html, body {
    width: 1200px; height: 864px; overflow: hidden;
    background: var(--page-bg);
    font-family: "Exo 2", sans-serif;
  }
  .stage {
    position: relative; width: 1200px; height: 864px;
  }
  .card {
    position: absolute;
    width: 560px; height: 340px;
    background: var(--card-bg);
    border: 1px solid var(--card-edge);
    border-radius: 4px;
  }
  .card--front { left: 30px; top: 120px; }
  .card--back { left: 610px; top: 404px; }

  .front-wordmark {
    position: absolute; inset: 0;
    display: flex; align-items: center; justify-content: center;
    color: var(--brand-silver);
    font-weight: 800; font-size: 46px; letter-spacing: 3px;
    text-transform: uppercase;
  }

  .back-wordmark {
    position: absolute; left: 34px; top: 120px; width: 220px;
    color: var(--brand-blue);
    font-weight: 800; font-size: 28px; line-height: 1.05; letter-spacing: 1px;
    text-transform: uppercase; text-align: center;
  }
  .back-wordmark span { display: block; font-size: 22px; letter-spacing: 2px; }

  .divider {
    position: absolute; left: 272px; top: 100px;
    width: 1px; height: 120px; background: var(--divider);
  }

  .contact {
    position: absolute; left: 292px; top: 104px;
    color: var(--text-light); font-size: 14px; line-height: 1.4;
  }
  .contact__name {
    color: var(--brand-blue); font-weight: 700; font-size: 18px;
    letter-spacing: 1px; text-transform: uppercase; margin-bottom: 6px;
  }
  .contact__address { margin-bottom: 2px; }
  .contact__row { display: flex; align-items: center; gap: 8px; }
  .contact__row svg { width: 11px; height: 11px; fill: var(--text-light); flex: none; }

  .taglines {
    position: absolute; left: 30px; top: 244px; width: 330px;
    color: var(--text-light); font-size: 14px; line-height: 1.45; text-align: center;
  }
</style>
</head>
<body>
<main class="stage">
  <section class="card card--front" aria-label="Business card front">
    <div class="front-wordmark">MRF Accountants</div>
  </section>

  <section class="card card--back" aria-label="Business card back">
    <div class="back-wordmark">MRF<span>Accountants</span></div>
    <div class="divider"></div>
    <div class="contact">
      <p class="contact__name">Marcus Elwin</p>
      <p class="contact__address">Level 5, 8 Corvale Ridge Road<br>ASHGROVE RISE VIC 3187</p>
      <p class="contact__row">
        <svg viewBox="0 0 12 12" aria-hidden="true"><path d="M2.5 0.5 L4.5 0.5 L5.3 3 L4 4.2 Q5.2 6.8 7.8 8 L9 6.7 L11.5 7.5 L11.5 9.5 Q11.5 11.5 9.5 11.5 Q0.5 10.8 0.5 2.5 Q0.5 0.5 2.5 0.5Z"/></svg>
        9481 3057
      </p>
      <p class="contact__row">
        <svg viewBox="0 0 12 12" aria-hidden="true"><path d="M0.5 2 H11.5 V10 H0.5Z M1 2.5 L6 6.5 L11 2.5" stroke="#1c1d1f" stroke-width="0.9"/></svg>
        melwin@mrfaccountants.com.au
      </p>
      <p class="contact__row">
        <svg viewBox="0 0 12 12" aria-hidden="true"><circle cx="6" cy="6" r="5.5"/><path d="M0.8 6 H11.2 M6 0.6 Q3 6 6 11.4 M6 0.6 Q9 6 6 11.4" stroke="#1c1d1f" stroke-width="0.8" fill="none"/></svg>
        www.mrfaccountants.com.au
      </p>
    </div>
    <p class="taglines">The end to your tax problems begin with us<br>A referral from you is our greatest compliment</p>
  </section>
</main>
</body>
</html>
```